Global Yoga Apparel Brand Needs a Beautiful Website

We need a website design for a new Yoga brand called Vessa. We develop beautiful, stylish, sexy, comfortable yoga leggings, tops, and yoga apparel for women looking to feel their best, look their best and perform their best on and off the yoga mat.
This will go up at http://vessa.example/ (which is a landing page right now).
We would like to see simple and clean design where the focus will be on powerful images and clean background space. We will be using Shopify to start building on and here are three sites that we would love to see options based off of the look, layout and feel while making something unique at the same time:
1. Tumo.ca
2. marikoven.com
3. www.q-plume.com
The final design should look clean, beautiful, inspiring, powerful and empowering.
Target Market(s)
mostly Females 21-35 range but will be appealing to women over 35 as well.

```html
<!DOCTYPE html>
<html lang="en">
<head>
<meta charset="utf-8">
<title>Vessa — Yoga Apparel</title>
<link rel="stylesheet" href="https://fonts.googleapis.com/css2?family=PT+Sans:wght@400;700&family=Open+Sans:wght@300;400;600&family=Montserrat:wght@400;500&display=swap">
<style>
:root{
  --ink:#111;
  --black:#000;
  --white:#fff;
  --panel:#f5f5f5;
  --section:#efefef;
  --muted:#555;
  --line:#ccc;
  --foot-text:#8a8a8a;
  --foot-line:#444;
}
*{box-sizing:border-box;margin:0;padding:0}
html,body{width:680px;height:1200px;overflow:hidden;background:var(--white)}
body{font-family:"Open Sans",sans-serif;color:var(--ink);position:relative}
.abs{position:absolute}
.btn{position:absolute;background:var(--ink);color:var(--white);font-family:"Montserrat",sans-serif;font-weight:500;font-size:5.5px;letter-spacing:.4px;display:flex;align-items:center;justify-content:center}

/* header */
.site-header{position:absolute;left:0;top:0;width:680px;height:40px;background:var(--black);color:var(--white)}
.brand{position:absolute;left:70px;top:10px;font-family:"PT Sans",sans-serif;font-weight:700;font-size:17px;line-height:20px;color:var(--white)}
.nav-marker{position:absolute;left:132px;top:0;width:20px;height:2px;background:var(--white)}
.main-nav{position:absolute;left:132px;top:16px;display:flex;gap:16px;font-family:"Montserrat",sans-serif;font-size:7px;letter-spacing:.4px}
.utility-nav{position:absolute;left:453px;top:16px;display:flex;gap:14px;font-family:"Montserrat",sans-serif;font-size:7px;letter-spacing:.4px;align-items:center}
.utility-nav span{display:flex;align-items:center;gap:4px}

/* hero */
.hero{position:absolute;left:0;top:40px;width:680px;height:262px;background:linear-gradient(90deg,#e9e9e9 0%,#f4f4f4 40%,#fbfbfb 100%)}
.hero-figure{position:absolute;left:60px;top:0;width:440px;height:262px;background:linear-gradient(160deg,#d9d4d1 0%,#3a3745 45%,#2b2a3a 70%,#e8e8e8 100%);opacity:.85;border-radius:0 0 40px 0}
.hero-copy{position:absolute;left:391px;top:88px;width:168px;display:flex;flex-direction:column;align-items:center}
.hero-title{width:168px;height:37px;border:2px solid var(--ink);background:var(--white);font-family:"PT Sans",sans-serif;font-weight:700;font-size:20px;display:flex;align-items:center;justify-content:center;letter-spacing:.5px}
.hero-note{margin-top:16px;font-size:7px;color:var(--ink);text-align:center}
.hero-copy .btn{position:static;margin-top:11px;width:46px;height:14px}

/* feature row */
.feature-row{position:absolute;left:0;top:302px;width:680px;height:164px}
.feature-photo{position:absolute;top:0;height:164px}
.feature-text{position:absolute;top:0;height:164px;padding:44px 0 0 23px}
.eyebrow{font-family:"Montserrat",sans-serif;font-size:4.5px;letter-spacing:1px}
.feature-title{font-family:"PT Sans",sans-serif;font-weight:700;font-size:9.5px;letter-spacing:.4px;margin-top:6px}
.feature-copy{font-size:5.5px;line-height:10px;margin-top:5px;width:100px}

/* products */
.tabs{position:absolute;left:0;top:490px;width:680px;display:flex;justify-content:center;align-items:center;font-family:"Open Sans",sans-serif;font-weight:300;font-size:21px;letter-spacing:1px;color:#333}
.tabs .divider{width:1px;height:16px;background:var(--line);margin:0 22px}
.tabs svg{margin-left:3px}
.tab-note{position:absolute;left:0;top:531px;width:680px;text-align:center;font-family:"Montserrat",sans-serif;font-weight:500;font-size:5.5px;letter-spacing:.4px}
.products{position:absolute;left:0;top:550px;width:680px;height:268px;background:var(--section)}
.card{position:absolute;top:17px;width:127px;height:182px;background:var(--white)}
.card .shot{width:127px;height:136px}
.card .name{text-align:center;font-family:"PT Sans",sans-serif;font-weight:700;font-size:7.5px;letter-spacing:.5px;margin-top:11px}
.card .price{text-align:center;font-size:7.5px;color:#444;margin-top:3px}
.card .price s{font-size:6px;color:#777;margin-right:2px}
.card.active{height:207px}
.load-more{position:absolute;left:0;top:236px;width:680px;text-align:center;font-family:"PT Sans",sans-serif;font-size:10.5px;letter-spacing:.7px;color:#333}

/* banner */
.banner{position:absolute;left:74px;top:841px;width:531px;height:217px;background:var(--panel)}
.banner-photo{position:absolute;left:0;top:0;width:250px;height:217px;background:linear-gradient(135deg,#b08a73 0%,#e8e2dc 35%,#4a4a4a 60%,#d9d9d9 85%)}
.banner-title{position:absolute;left:273px;top:60px;font-family:"PT Sans",sans-serif;font-weight:700;font-size:21px;letter-spacing:.6px}
.banner-copy{position:absolute;left:273px;top:96px;width:170px;font-size:5.5px;line-height:10px}
.dots{position:absolute;left:273px;top:183px;display:flex;gap:3px}
.dots i{display:block;width:10px;height:1px;background:#ddd}
.dots i.on{background:var(--ink)}

/* footer */
.site-footer{position:absolute;left:0;top:1082px;width:680px;height:118px;background:var(--black);color:var(--foot-text)}
.footer-brand{position:absolute;left:70px;top:25px;font-family:"PT Sans",sans-serif;font-weight:700;font-size:17px;color:var(--white)}
.footer-col{position:absolute;top:22px;font-family:"Montserrat",sans-serif;font-size:5.5px;letter-spacing:.5px;line-height:11.3px}
.footer-col h4{font-weight:500;font-size:5.5px;color:#b5b5b5;margin-bottom:5px}
.social{position:absolute;left:435px;top:17px;display:flex;gap:5px}
.social span{width:23px;height:23px;border:1px solid var(--foot-line);display:flex;align-items:center;justify-content:center}
.social span i{width:7px;height:7px;background:#777;display:block}
.newsletter{position:absolute;left:435px;top:56px;width:163px;border-bottom:1px solid var(--foot-line);padding-bottom:5px;font-size:5.5px;display:flex;align-items:center;gap:5px}
.copyright{position:absolute;left:0;top:98px;width:680px;text-align:center;font-size:4.5px;color:#666}
</style>
</head>
<body>

<header class="site-header">
  <div class="nav-marker"></div>
  <div class="brand">Vessa</div>
  <nav class="main-nav"><span>HOME</span><span>NEW ARRIVAL</span><span>POPULAR</span><span>WOMEN</span><span>MEN</span></nav>
  <div class="utility-nav">
    <span><svg width="7" height="7" viewBox="0 0 10 10"><circle cx="4" cy="4" r="3" fill="none" stroke="#fff" stroke-width="1.4"/><line x1="6.2" y1="6.2" x2="9.5" y2="9.5" stroke="#fff" stroke-width="1.4"/></svg>SEARCH</span>
    <span><svg width="7" height="7" viewBox="0 0 10 10"><path d="M1 3h8l-1 6H2z" fill="#fff"/><path d="M3 3a2 2 0 0 1 4 0" fill="none" stroke="#fff"/></svg>CART (2)</span>
    <span><svg width="7" height="7" viewBox="0 0 10 10"><circle cx="5" cy="3" r="2.3" fill="#fff"/><path d="M0.8 10a4.2 4 0 0 1 8.4 0z" fill="#fff"/></svg>SIGN IN</span>
  </div>
</header>

<section class="hero">
  <div class="hero-figure" role="img" aria-label="Woman in a navy yoga outfit holding an upward-facing dog pose in a bright white studio"></div>
  <div class="hero-copy">
    <div class="hero-title">SUMMER SALE</div>
    <div class="hero-note">Up to 70% Off</div>
    <div class="btn">GRAB IT NOW</div>
  </div>
</section>

<section class="feature-row">
  <div class="feature-photo" style="left:0;width:208px;background:linear-gradient(120deg,#f3f3f3 0%,#cfcfcf 45%,#5a5a5a 65%,#ececec 100%)" role="img" aria-label="Woman in grey leggings and a black top doing a camel pose"></div>
  <div class="feature-text" style="left:208px;width:132px;background:var(--panel)">
    <div class="eyebrow">JUST ARRIVED</div>
    <div class="feature-title">SUMMER ESSENTIALS</div>
    <div class="feature-copy">Make your Yoga practices become more comfortable</div>
    <div class="btn" style="left:23px;top:106px;width:46px;height:14px">GET IT NOW</div>
  </div>
  <div class="feature-photo" style="left:340px;width:207px;background:linear-gradient(180deg,#f2f2f2 0%,#d4d4d4 45%,#3c3c3c 75%,#e6e6e6 100%)" role="img" aria-label="Woman seated cross-legged seen from behind with hands in reverse prayer"></div>
  <div class="feature-text" style="left:547px;width:133px;background:var(--black);color:var(--white)">
    <div class="eyebrow">MOST POPULAR</div>
    <div class="feature-title">COLORFUL PANT</div>
    <div class="feature-copy">Make your Yoga practices become more comfortable</div>
    <div class="btn" style="left:23px;top:106px;width:46px;height:14px;background:var(--white);color:var(--ink)">GET IT NOW</div>
  </div>
</section>

<div class="tabs">
  <span>POPULAR</span><svg width="8" height="5" viewBox="0 0 8 5"><path d="M0.5 0.5 4 4 7.5 0.5" fill="none" stroke="#333"/></svg>
  <span class="divider"></span>
  <span>ARRIVALS</span><svg width="8" height="5" viewBox="0 0 8 5"><path d="M0.5 0.5 4 4 7.5 0.5" fill="none" stroke="#333"/></svg>
</div>
<div class="tab-note">WE HAVE OVER 2000 PRODUCTS IN OUR SHOP</div>

<section class="products">
  <article class="card" style="left:78px">
    <div class="shot" role="img" aria-label="Woman in slim grey pants seated on a mat" style="background:linear-gradient(180deg,#f4f4f4 0%,#d8d8d8 55%,#7a7a7a 80%,#e4e4e4 100%)"></div>
    <div class="name">SLIM PANTS</div><div class="price">$279,00</div>
  </article>
  <article class="card active" style="left:210px">
    <div class="shot" role="img" aria-label="Woman in navy pants holding a warrior pose" style="background:linear-gradient(180deg,#f5f5f5 0%,#cfd2d8 50%,#3a4050 78%,#e8e8e8 100%)"></div>
    <div class="name">LOW SLIM PANTS</div><div class="price"><s>$329,00</s>$279,00</div>
    <div class="btn" style="left:23px;top:180px;width:81px;height:14px;font-size:5.5px">ADD TO CART</div>
  </article>
  <article class="card" style="left:342px">
    <div class="shot" role="img" aria-label="Woman in blue top and grey pants in a lunge with arms raised" style="background:linear-gradient(180deg,#f1f1f1 0%,#c6d0da 45%,#5d6878 72%,#2f4555 100%)"></div>
    <div class="name">GUMMI PANT</div><div class="price">$279,00</div>
  </article>
  <article class="card" style="left:475px">
    <div class="shot" role="img" aria-label="Woman in red top and black leggings in a wide stance on a wooden floor" style="background:linear-gradient(180deg,#f2f2f2 0%,#dcdcdc 45%,#4a4a4a 70%,#c59a63 100%)"></div>
    <div class="name">YOGA JEANS</div><div class="price">$279,00</div>
  </article>
  <div class="load-more">+ LOAD MORE PRODUCTS</div>
</section>

<section class="banner">
  <div class="banner-photo" role="img" aria-label="Woman in patterned leggings stretching one leg high"></div>
  <div class="banner-title">SUMMER HEATS</div>
  <div class="banner-copy">The hottest styles for summer are here. Shop beach-ready bikinis in your favorite fits, colors and patterns</div>
  <div class="btn" style="left:273px;top:129px;width:80px;height:14px">SHOP COLLECTION NOW</div>
  <div class="dots"><i class="on"></i><i></i><i></i><i></i></div>
  <svg class="abs" style="left:496px;top:105px" width="8" height="14" viewBox="0 0 8 14"><path d="M1 1 7 7 1 13" fill="none" stroke="#bbb" stroke-width="1.2"/></svg>
</section>

<footer class="site-footer">
  <div class="footer-brand">Vessa</div>
  <div class="footer-col" style="left:126px"><h4>SHOP</h4>PANTS<br>ACCESSORIES<br>BRANDS<br>CLEARANCE</div>
  <div class="footer-col" style="left:215px"><h4>USEFUL LINKS</h4>ABOUT<br>CONTACT US<br>SUPPORT<br>STORE LOCATOR</div>
  <div class="footer-col" style="left:303px"><h4>TERM &amp; CONDITIONS</h4>WEBSITE TERMS<br>PRESS ROOM</div>
  <div class="social"><span><i></i></span><span><i></i></span><span><i></i></span><span><i></i></span></div>
  <div class="newsletter"><svg width="7" height="5" viewBox="0 0 7 5"><rect x="0.3" y="0.3" width="6.4" height="4.4" fill="none" stroke="#777" stroke-width="0.6"/><path d="M0.3 0.3 3.5 3 6.7 0.3" fill="none" stroke="#777" stroke-width="0.6"/></svg>Suscribe our newsletter...</div>
  <div class="copyright">Copyright © 2016 Vessa. All rights reserved.</div>
</footer>

</body>
</html>
```